Ridgefold MMA - Ridgefold Way - 7-5-4

This will be for a wall logo. Probably printed on vinyl to adhere to the wall. This a rough draft concept of the project, but we're certainly open to other designs. Red, Black and White are the main colors we would like to use. The triangle motif is important, it denotes stability and base, which are important in jiu jistu.
The Ridgefold Way (7-5-4)
7 Virtues of a Warrior (Bushido)
R Rectitude
Doing what is right w/o regard for the consequences
C Courage
Inner strength to resist opposition. Courage not just to step on the mat but to make the right decisions
B Benevolence
Mindset to do good. Be kind and generous
P Politeness
Proper consideration and courtesy to others
L Loyalty
Faithfulness & Alliance. Not blind allegiance
H Honesty / Sincerity
Be a man of your word. Do what you say you will
Genuine Integrity in character & action
H Honor
Profound respect & ethical conduct
Make the right decisions to be worthy of respectability
5 Keys to Health
Nutrition - Eat sensibly
Exercise - Stay fit and ready
Rest - Recovery and Recharge
Hygiene - Stay Clean
Attitude - Assume positive intent
Look at life in a positive way
4 States of Mind (Spirit of Budo)
Shoshin - Beginners Mind
Be open to new ideas
Eager to Learn
Zanshin – Remaining Mind
Being Alert and Aware, but relaxed
Be Prepared
Mushin – No Mind (Clear Mind)
Be able to act in the moment without having to think
Fudoshin – Immovable Mind
Emotional Balance
Free from anger, fear, & doubt

```html
<!DOCTYPE html>
<html lang="en">
<head>
<meta charset="utf-8">
<title>The Ridgefold Way 7 5 4</title>
<link href="https://fonts.googleapis.com/css2?family=Montserrat:wght@500;600;700;800;900&display=swap" rel="stylesheet">
<style>
  :root {
    --red: #e3000f;
    --red-deep: #a8000a;
    --black: #000000;
    --white: #ffffff;
    --stage: #3a3a3a;
    --photo-dark: #2a2a2a;
    --photo-light: #cfcfcf;
  }
  * { margin: 0; padding: 0; box-sizing: border-box; }
  html, body {
    width: 1200px; height: 2378px; overflow: hidden;
    background: var(--stage);
    font-family: "Montserrat", sans-serif;
  }
  .stage { position: relative; width: 1200px; height: 2378px; }
  .poster {
    position: absolute; left: 80px; top: 461px;
    width: 674px; height: 944px;
    transform: scale(1.543); transform-origin: 0 0;
    background: var(--red); overflow: hidden; color: var(--white);
    box-shadow: 0 4px 14px rgba(0,0,0,.5);
  }
  .poster__shapes { position: absolute; inset: 0; width: 674px; height: 944px; }
  .title {
    position: absolute; left: 38px; top: 26px;
    font-size: 38px; font-weight: 800; letter-spacing: .5px; line-height: 1;
    white-space: nowrap;
  }
  .code-tab {
    position: absolute; left: 506px; top: 31px; width: 180px; height: 41px;
    background: var(--white); border-radius: 22px 0 0 22px;
    color: var(--black); font-size: 38px; font-weight: 900; font-style: italic;
    line-height: 41px; padding-left: 12px; letter-spacing: 10px;
  }
  .subtitle-pill {
    position: absolute; left: 118px; top: 88px; width: 438px; height: 33px;
    background: var(--white); border-radius: 17px;
    color: var(--black); font-size: 25px; font-weight: 800;
    text-align: center; line-height: 33px; white-space: nowrap;
  }
  .virtue { position: absolute; }
  .virtue__name { font-size: 20px; font-weight: 800; line-height: 1; white-space: nowrap; }
  .virtue__desc { font-size: 10.5px; font-weight: 600; line-height: 14px; margin-top: 1px; }
  .section-title {
    position: absolute; left: 38px;
    font-size: 29px; font-weight: 800; line-height: 29px;
  }
  .checklist { position: absolute; left: 38px; list-style: none; }
  .checklist li {
    display: flex; align-items: center; white-space: nowrap;
    font-size: 16px; font-weight: 600;
  }
  .checklist li strong { font-weight: 800; margin-right: 5px; }
  .tick { width: 11px; height: 11px; margin: 0 11px 0 2px; flex: none; }
  .health li { height: 25.5px; }
  .mind li { height: 27px; font-weight: 800; }
  .health__extra {
    position: absolute; left: 62px; top: 606px;
    font-size: 19px; font-weight: 600; white-space: nowrap;
  }
</style>
</head>
<body>
<main class="stage">
  <article class="poster">
    <svg class="poster__shapes" viewBox="0 0 674 944" aria-hidden="false">
      <defs>
        <radialGradient id="figureTone" cx="0.7" cy="0.35" r="0.55">
          <stop offset="0" stop-color="var(--red-deep)" stop-opacity=".75"/>
          <stop offset="1" stop-color="var(--red)" stop-opacity="0"/>
        </radialGradient>
        <linearGradient id="photoTone" x1="0" y1="0" x2="1" y2="1">
          <stop offset="0" stop-color="var(--photo-dark)"/>
          <stop offset=".7" stop-color="#5a1a1a"/>
          <stop offset="1" stop-color="var(--photo-light)"/>
        </linearGradient>
      </defs>
      <rect class="backdrop-photo" x="180" y="130" width="494" height="580" fill="url(#figureTone)"
            role="img" aria-label="Faded red-toned photo of two grapplers training on the mat"/>
      <polygon class="base-triangle" points="0,273 674,653 674,944 0,944" fill="var(--black)"/>
      <polygon class="accent-stripe" points="172,944 674,654 674,944" fill="var(--white)"/>
      <polygon class="action-photo" points="198,944 674,672 674,944" fill="url(#photoTone)"
               role="img" aria-label="Photo of two jiu-jitsu athletes grappling, seen from above"/>
    </svg>

    <h1 class="title">THE RIDGEFOLD WAY</h1>
    <div class="code-tab">754</div>
    <h2 class="subtitle-pill">7 VIRTUES OF A WARRIOR</h2>

    <div class="virtue" style="left:38px;top:158px">
      <div class="virtue__name">R RECTITUDE</div>
      <div class="virtue__desc">Doing what is right w/o regard for the consequences</div>
    </div>
    <div class="virtue" style="left:60px;top:201px">
      <div class="virtue__name">C COURAGE</div>
      <div class="virtue__desc">Inner strength to resist opposition. Courage not just to step on the mat but<br>to make the right decisions</div>
    </div>
    <div class="virtue" style="left:93px;top:257px">
      <div class="virtue__name">B BENEVOLENCE</div>
      <div class="virtue__desc">Mindset to do good. Be kind and generous</div>
    </div>
    <div class="virtue" style="left:162px;top:301px">
      <div class="virtue__name">P POLITENESS</div>
      <div class="virtue__desc">Proper consideration and courtesy to others</div>
    </div>
    <div class="virtue" style="left:218px;top:341px">
      <div class="virtue__name">L LOYALTY</div>
      <div class="virtue__desc">Faithfulness &amp; Alliance. Not blind allegiance</div>
    </div>
    <div class="virtue" style="left:282px;top:386px">
      <div class="virtue__name">H HONESTY / SINCERITY</div>
      <div class="virtue__desc" style="padding-left:4px">Be a man of your word. Do what you say you will. Genuine<br><span style="padding-left:14px">Integrity in character &amp; action</span></div>
    </div>
    <div class="virtue" style="left:392px;top:452px">
      <div class="virtue__name">H HONOR</div>
      <div class="virtue__desc" style="padding-left:25px">Profound respect &amp; ethical conduct. Make<br><span style="padding-left:14px">the right decisions to be worthy of</span><br><span style="padding-left:38px">respectability</span></div>
    </div>

    <h2 class="section-title" style="top:404px">5 KEYS<br>TO HEALTH</h2>
    <ul class="checklist health" style="top:472px">
      <li><svg class="tick" viewBox="0 0 12 12"><circle cx="6" cy="6" r="6" fill="var(--red)"/><path d="M3.2 6.2l1.9 1.9 3.7-4" stroke="var(--white)" stroke-width="1.6" fill="none"/></svg><strong>NUTRITION</strong>- Eat sensibly</li>
      <li><svg class="tick" viewBox="0 0 12 12"><circle cx="6" cy="6" r="6" fill="var(--red)"/><path d="M3.2 6.2l1.9 1.9 3.7-4" stroke="var(--white)" stroke-width="1.6" fill="none"/></svg><strong>EXERCISE</strong>- Stay fit and ready</li>
      <li><svg class="tick" viewBox="0 0 12 12"><circle cx="6" cy="6" r="6" fill="var(--red)"/><path d="M3.2 6.2l1.9 1.9 3.7-4" stroke="var(--white)" stroke-width="1.6" fill="none"/></svg><strong>REST</strong>- Recovery and Recharge</li>
      <li><svg class="tick" viewBox="0 0 12 12"><circle cx="6" cy="6" r="6" fill="var(--red)"/><path d="M3.2 6.2l1.9 1.9 3.7-4" stroke="var(--white)" stroke-width="1.6" fill="none"/></svg><strong>HYGIENE</strong>- Stay Clean</li>
      <li><svg class="tick" viewBox="0 0 12 12"><circle cx="6" cy="6" r="6" fill="var(--red)"/><path d="M3.2 6.2l1.9 1.9 3.7-4" stroke="var(--white)" stroke-width="1.6" fill="none"/></svg><strong>ATTITUDE</strong>- Assume positive intent</li>
    </ul>
    <p class="health__extra">Look at life in a positive way</p>

    <h2 class="section-title" style="top:685px">4 STATES OF MIND</h2>
    <ul class="checklist mind" style="top:720px">
      <li><svg class="tick" viewBox="0 0 12 12"><circle cx="6" cy="6" r="6" fill="var(--red)"/><path d="M3.2 6.2l1.9 1.9 3.7-4" stroke="var(--white)" stroke-width="1.6" fill="none"/></svg>SHOSHIN - BEGINNERS MIND</li>
      <li><svg class="tick" viewBox="0 0 12 12"><circle cx="6" cy="6" r="6" fill="var(--red)"/><path d="M3.2 6.2l1.9 1.9 3.7-4" stroke="var(--white)" stroke-width="1.6" fill="none"/></svg>ZANSHIN – REMAINING MIND</li>
      <li><svg class="tick" viewBox="0 0 12 12"><circle cx="6" cy="6" r="6" fill="var(--red)"/><path d="M3.2 6.2l1.9 1.9 3.7-4" stroke="var(--white)" stroke-width="1.6" fill="none"/></svg>MUSHIN – NO MIND</li>
      <li><svg class="tick" viewBox="0 0 12 12"><circle cx="6" cy="6" r="6" fill="var(--red)"/><path d="M3.2 6.2l1.9 1.9 3.7-4" stroke="var(--white)" stroke-width="1.6" fill="none"/></svg>FUDOSHIN – IMMOVABLE MIND</li>
    </ul>
  </article>
</main>
</body>
</html>
```